Design CD-Velvet Tadpole/WAIT FOR THE ORANGE TRAIN
Zielgruppe
Wir sind Velvet Tadpole eine INDIE/ALTERNATIVE Band.. bestehend aus 4 Jungs im alter von durchschnittlich 22 Jahren. Wir suchen ein Design für unsere 2. Platte die den Namen 'WAIT FOR THE ORANGE TRAIN' trägt. Im gleichnamigen Song geht es um einen Menschen der am Limit lebt und jeden Moment ohne Rücksicht auf andere auskostet.. als er eines Tages versteht wie er den Menschen die er liebt damit Schaden zufügt, verspricht er seiner LIEBE:'I SWEAR I WILL WAIT FOR THE ORANGE TRAIN'..'im nächsten Leben werde ich ein besserer Typ sein.
Unsere Musik zeichnet sich durch 3 Stimmigen Gesang, verspielte teilweise psychodelische Sounds und eingängige Melodien die sich zu unserem Markenzeichen entwickelt haben aus.
Aufgabenstellung
Das Design soll Modern,verspielt,Bunt, gerne etwas abstrakt und vor allem Grafisch (nicht im realistic style) sein.
Beispielbilder in welche Richtung es gehen soll lege ich in den Anhang.

```html
<!DOCTYPE html>
<html lang="en">
<head>
<meta charset="utf-8">
<title>Velvet Tadpole – Wait for the Orange Train</title>
<link rel="stylesheet" href="https://fonts.googleapis.com/css2?family=Anton&display=swap">
<style>
  :root {
    --stage: #3a3a3a;
    --cover-light: #e9e9e9;
    --cover-mid: #9a9a9a;
    --cover-dark: #1c1c1c;
    --title-purple: #4b1f86;
    --band-black: #161616;
    --ghost-grey: rgba(60, 60, 60, 0.35);
  }
  html, body {
    margin: 0;
    width: 1200px;
    height: 1200px;
    overflow: hidden;
    background: var(--stage);
  }
  .cover {
    position: absolute;
    left: 100px;
    top: 100px;
    width: 1000px;
    height: 1000px;
    overflow: hidden;
    border: 2px solid #cfcfcf;
    box-sizing: border-box;
  }
  .cover-art {
    position: absolute;
    inset: 0;
    background:
      radial-gradient(ellipse at 20% 25%, var(--cover-dark) 0%, transparent 30%),
      radial-gradient(ellipse at 70% 70%, var(--cover-dark) 0%, transparent 28%),
      radial-gradient(ellipse at 35% 70%, var(--cover-mid) 0%, transparent 35%),
      radial-gradient(ellipse at 85% 25%, var(--cover-mid) 0%, transparent 30%),
      var(--cover-light);
  }
  .album-title {
    position: absolute;
    left: 540px;
    top: 30px;
    margin: 0;
    font-family: "Anton", sans-serif;
    font-weight: 400;
    font-size: 78px;
    line-height: 80px;
    letter-spacing: 3px;
    color: var(--title-purple);
    text-shadow: 18px 22px 0 var(--ghost-grey);
  }
  .album-title span { display: block; }
  .band-name {
    position: absolute;
    left: 330px;
    top: 820px;
    margin: 0;
    font-family: "Anton", sans-serif;
    font-weight: 400;
    font-size: 76px;
    letter-spacing: 3px;
    color: var(--band-black);
    text-shadow: -20px 24px 0 var(--ghost-grey);
    white-space: nowrap;
  }
</style>
</head>
<body>
  <main class="cover">
    <div class="cover-art" role="img" aria-label="Abstract black and white liquid chrome pattern with swirling metallic shapes"></div>
    <h1 class="album-title">
      <span>WAIT</span>
      <span>FOR</span>
      <span>THE</span>
      <span>ORANGE</span>
      <span>TRAIN</span>
    </h1>
    <p class="band-name">Velvet Tadpole</p>
  </main>
</body>
</html>
```